Business Cards for a Luggage Service (Repair, Sales, Warranty Etc.) Company
Belmora Baggage Services
Professional
Gregory Talvane
Owner
2418 Quillon Ave. Suite 320 Atlanta, GA 30987
Info@BelmoraBaggageServices.example
www.BelmoraBaggageServices.example
The logo was made for my sign. So it's a bit big.
tkalvin tkalvin
Our company is a luggage service company. We repair luggage, provide warranty related services, and sell new luggage. We are located within 1 mile of Atlanta's Pembrook Dallow International Airport (worlds busiest airport). We specialize in flight crew luggage repair and services.

```html
<!DOCTYPE html>
<html lang="en">
<head>
<meta charset="utf-8">
<title>Belmora Baggage Services – Business Card</title>
<link href="https://fonts.googleapis.com/css2?family=Roboto+Condensed:ital,wght@0,400;0,700;1,700&display=swap" rel="stylesheet">
<style>
  :root {
    --red: #e0212b;
    --black: #1a1a1a;
    --ink: #262626;
    --grey: #6b6b6b;
    --paper: #ffffff;
    --backdrop: #d8d8d8;
  }
  html, body {
    margin: 0;
    width: 1200px;
    height: 1077px;
    overflow: hidden;
    background: var(--backdrop);
    font-family: "Roboto Condensed", Arial, sans-serif;
    color: var(--ink);
  }
  .card {
    position: absolute;
    left: 120px;
    width: 960px;
    height: 500px;
    background: var(--paper);
    box-shadow: 0 4px 14px rgba(0,0,0,.18);
    overflow: hidden;
  }
  .card--back { top: 24px; }
  .card--front { top: 553px; }

  .brand {
    position: absolute;
    display: flex;
    align-items: center;
    gap: 18px;
  }
  .brand__mark {
    width: 62px;
    height: 62px;
    background: var(--red);
    flex: none;
  }
  .brand__name {
    font-size: 40px;
    font-weight: 700;
    color: var(--black);
    line-height: 1.05;
    width: 300px;
  }
  .brand__services {
    position: absolute;
    font-size: 13px;
    letter-spacing: 2px;
    color: var(--grey);
    text-transform: uppercase;
  }

  /* back side */
  .card--back .brand { left: 60px; top: 190px; }
  .card--back .brand__services { left: 60px; top: 310px; }
  .contact {
    position: absolute;
    left: 440px;
    top: 60px;
    font-style: italic;
    font-weight: 700;
    font-size: 17px;
    line-height: 1.5;
  }
  .contact__title, .social__title {
    font-size: 24px;
    text-transform: uppercase;
    margin-bottom: 6px;
    color: var(--black);
  }
  .social {
    position: absolute;
    left: 600px;
    top: 240px;
    font-style: italic;
    font-weight: 700;
    font-size: 17px;
    line-height: 1.5;
  }
  .back-band {
    position: absolute;
    left: 0; right: 0; bottom: 0;
    height: 28px;
    background: var(--red);
  }

  /* front side */
  .front-band {
    position: absolute;
    left: 0; right: 0;
    top: 40px;
    height: 34px;
    background: var(--red);
  }
  .front-band__block {
    position: absolute;
    left: 220px;
    top: 0;
    width: 90px;
    height: 34px;
    background: var(--black);
  }
  .card--front .brand { left: 60px; top: 190px; }
  .card--front .brand__services { left: 60px; top: 310px; }
  .person {
    position: absolute;
    right: 70px;
    top: 240px;
    text-align: left;
  }
  .person__name {
    font-size: 30px;
    font-weight: 700;
    text-transform: uppercase;
    color: var(--black);
  }
  .person__role {
    font-size: 18px;
    text-transform: uppercase;
    color: var(--grey);
    margin-top: 4px;
  }
  .front-stripe {
    position: absolute;
    right: 0;
    top: 340px;
    width: 420px;
    height: 20px;
    background: var(--red);
  }
</style>
</head>
<body>

<section class="card card--back" aria-label="Card back">
  <div class="brand">
    <div class="brand__mark"></div>
    <div class="brand__name">Belmora Baggage Services</div>
  </div>
  <div class="brand__services">Repairs · Warranty · Sales</div>

  <div class="contact">
    <div class="contact__title">Contact Us</div>
    <div>012 345 6789</div>
    <div>Info@BelmoraBaggageServices.example</div>
    <div>www.BelmoraBaggageServices.example</div>
  </div>

  <div class="social">
    <div class="social__title">Follow Us on Social</div>
    <div>facelink.example/user-name</div>
    <div>chirpline.example/user-name</div>
    <div>folioboard.example/user-name</div>
  </div>

  <div class="back-band"></div>
</section>

<section class="card card--front" aria-label="Card front">
  <div class="front-band"><div class="front-band__block"></div></div>

  <div class="brand">
    <div class="brand__mark"></div>
    <div class="brand__name">Belmora Baggage Services</div>
  </div>
  <div class="brand__services">Repairs · Warranty · Sales</div>

  <div class="person">
    <div class="person__name">Gregory Talvane</div>
    <div class="person__role">Founder</div>
  </div>

  <div class="front-stripe"></div>
</section>

</body>
</html>
```